Thriving Mexican import business needs a new business card

Need a refresher of our current business card. Looking for a lighter background with the logo on one side. We will want this file to be adjustable so we can change names, emails and mobile numbers.
We are open to ideas but maintaining a professional image is critical.
Thankyou,

Target Market(s)

Anyone in food industry

Industry/Entity Type

Wholesale

Contact Information for Business Card

Mark Pendlebury
Director
Condor Provisions & Spirits Pty Ltd
5B Morrow Ct, Kelvinbrook VIC 3127
0421930576 (03) 95128460
mark@condorlatino.example.au
condorlatinoprovisionsandspirits.example.au

Font styles to use
Serif
Other font styles liked:
• NeoGram Heavy

Requirements
Must have
• Professional yet memorable
Condor logo
Nice to have
• Chilli or tequila/mexican food pictures
Should not have
• Dark background

```html
<!DOCTYPE html>
<html lang="en">
<head>
<meta charset="utf-8">
<title>Condor Provisions &amp; Spirits — Business Card</title>
<link rel="stylesheet" href="https://fonts.googleapis.com/css2?family=Questrial&display=swap">
<style>
  :root {
    --page-bg: #2d3436;
    --panel: #f1ebe2;
    --paper: #ffffff;
    --brand-ink: #1c1a18;
    --text: #111111;
    --text-soft: #333333;
    --photo-light: #f4ebde;
    --photo-warm: #e6d2b6;
    --photo-accent: #d9b48f;
  }
  * { box-sizing: border-box; margin: 0; padding: 0; }
  html, body {
    width: 1013px; height: 1200px; overflow: hidden;
    background: var(--page-bg);
    font-family: "Questrial", "Century Gothic", sans-serif;
  }
  .card {
    position: absolute;
    left: 211px;
    width: 590px;
    height: 337px;
    overflow: hidden;
  }
  .card--front { top: 237px; display: flex; background: var(--paper); }
  .card--back { top: 640px; background: var(--photo-light); }

  .brand-panel {
    width: 260px; height: 100%;
    background: var(--panel);
    display: flex; align-items: center; justify-content: center;
  }
  .brand {
    display: flex; align-items: center; gap: 10px;
    color: var(--brand-ink);
    font-size: 36px;
    letter-spacing: 2px;
    text-transform: uppercase;
  }
  .brand__mark {
    width: 14px; height: 14px;
    background: var(--brand-ink);
  }

  .details { flex: 1; padding: 60px 0 0 17px; color: var(--text); }
  .details__name { font-size: 25px; font-weight: 400; letter-spacing: 0.3px; line-height: 1.15; -webkit-text-stroke: 0.4px var(--text); }
  .details__role { font-size: 16px; color: var(--text-soft); line-height: 1.2; letter-spacing: 0.5px; }
  .details__company {
    margin: 30px 0 14px -4px;
    font-size: 17px; color: var(--text-soft); letter-spacing: 0.6px;
  }
  .contact-list { list-style: none; margin-left: -4px; }
  .contact-list li {
    display: flex; align-items: center; gap: 7px;
    height: 28.7px;
    font-size: 13.8px; color: var(--text);
    white-space: nowrap;
  }
  .contact-list svg { width: 17px; height: 17px; flex: none; }

  .back-photo {
    position: absolute; inset: 0;
    background:
      radial-gradient(ellipse at 30% 70%, var(--photo-accent) 0%, transparent 55%),
      radial-gradient(ellipse at 80% 40%, var(--photo-warm) 0%, transparent 60%),
      linear-gradient(180deg, var(--photo-light) 0%, var(--photo-warm) 100%);
  }
  .back-brand {
    position: absolute; inset: 0;
    display: flex; align-items: center; justify-content: center;
  }
  .back-brand .brand { font-size: 50px; gap: 14px; }
  .back-brand .brand__mark { width: 19px; height: 19px; }
</style>
</head>
<body>

<section class="card card--front">
  <div class="brand-panel">
    <div class="brand"><span class="brand__mark"></span>Condor</div>
  </div>
  <div class="details">
    <h1 class="details__name">Mark Pendlebury</h1>
    <p class="details__role">Director</p>
    <p class="details__company">Condor Provisions &amp; Spirits Pty Ltd</p>
    <ul class="contact-list">
      <li>
        <svg viewBox="0 0 20 20" fill="none" stroke="#111" stroke-width="1.4"><circle cx="10" cy="10" r="8.8"/><path d="M10 15.5s-3.6-4-3.6-6.6a3.6 3.6 0 0 1 7.2 0c0 2.6-3.6 6.6-3.6 6.6z" fill="#111"/><circle cx="10" cy="8.8" r="1.3" fill="#fff" stroke="none"/></svg>
        5B Morrow Ct, Kelvinbrook VIC 3127
      </li>
      <li>
        <svg viewBox="0 0 20 20" fill="none" stroke="#111" stroke-width="1.4"><circle cx="10" cy="10" r="8.8"/><path d="M7.2 5.5l1.6 2.2-1 1.2c.6 1.4 1.7 2.5 3.1 3.1l1.2-1 2.2 1.6-.9 1.6c-3.8-.3-6.9-3.4-7.2-7.2z"/></svg>
        0421930576 (03) 95128460
      </li>
      <li>
        <svg viewBox="0 0 20 20" fill="none" stroke="#111" stroke-width="1.4"><circle cx="10" cy="10" r="8.8"/><rect x="5.5" y="6.8" width="9" height="6.4"/><path d="M5.5 7l4.5 3.4L14.5 7"/></svg>
        mark@condorlatino.example.au
      </li>
      <li>
        <svg viewBox="0 0 20 20" fill="none" stroke="#111" stroke-width="1.2"><circle cx="10" cy="10" r="8.8"/><circle cx="10" cy="10" r="5"/><ellipse cx="10" cy="10" rx="2.2" ry="5"/><path d="M5 10h10"/></svg>
        condorlatinoprovisionsandspirits.example.au
      </li>
    </ul>
  </div>
</section>

<section class="card card--back">
  <div class="back-photo" role="img" aria-label="Softly lit photograph of a Mexican food spread with plates, bottles of beer and tequila on a wooden table"></div>
  <div class="back-brand">
    <div class="brand"><span class="brand__mark"></span>Condor</div>
  </div>
</section>

</body>
</html>
```